Software static HTML page design

We need 5 static HTML pages designed for our current software startup - TallyNest. All details are attached in a document for consideration.

Target Market(s)

Sporting clubs/University clubs

Industry/Entity Type

Software

Number of Pages Required

5+ page

Font styles to use
Sans Serif

Colors
33a6d7
85cae6
86cfc6
33b8a4
ffffff

```html
<!DOCTYPE html>
<html lang="en">
<head>
<meta charset="utf-8">
<title>TallyNest – Bringing your club to the Social Web</title>
<link rel="stylesheet" href="https://fonts.googleapis.com/css2?family=Open+Sans:wght@400;600&display=swap">
<style>
  :root {
    --brand-blue: #33a6d7;
    --brand-blue-light: #85cae6;
    --brand-teal: #86cfc6;
    --brand-green: #33b8a4;
    --white: #ffffff;
    --text-grey: #555b66;
    --navy: #2d3f6e;
    --social-blue: #3b5497;
    --social-blue-dark: #2d4179;
    --night-deep: #050d3a;
    --night-mid: #0b2fa8;
    --night-glow: #2f7de0;
  }
  * { box-sizing: border-box; margin: 0; padding: 0; }
  html, body { width: 1200px; height: 674px; overflow: hidden; }
  body { font-family: "Open Sans", Arial, sans-serif; background: var(--white); position: relative; }

  .site-header { position: absolute; left: 0; top: 0; width: 1200px; height: 85px; background: var(--white); }
  .brand { position: absolute; left: 99px; top: 29px; display: flex; align-items: center; gap: 7px; }
  .brand-square { width: 14px; height: 14px; background: var(--brand-blue); }
  .brand-name { font-size: 24px; font-weight: 600; color: var(--brand-blue); letter-spacing: 0.5px; }

  .main-nav a { position: absolute; top: 36px; font-size: 14px; color: var(--text-grey); text-decoration: none; }
  .main-nav a.is-active { color: var(--brand-blue); }

  .header-btn { position: absolute; top: 29px; width: 86px; height: 34px; border-radius: 3px;
    font-size: 14px; font-weight: 600; display: flex; align-items: center; justify-content: center; text-decoration: none; }
  .header-btn--login { left: 920px; background: var(--brand-blue); color: var(--white); }
  .header-btn--signup { left: 1015px; border: 1px solid var(--brand-blue); color: var(--brand-blue); }

  .hero { position: absolute; left: 0; top: 85px; width: 1200px; height: 589px;
    background:
      radial-gradient(ellipse 260px 200px at 640px 240px, rgba(120,190,255,0.55), transparent 70%),
      radial-gradient(ellipse 300px 160px at 600px 560px, rgba(60,150,255,0.6), transparent 70%),
      linear-gradient(115deg, rgba(80,200,255,0.35) 0%, transparent 30%),
      linear-gradient(245deg, rgba(80,220,255,0.35) 0%, transparent 28%),
      linear-gradient(180deg, var(--night-deep) 0%, var(--night-mid) 55%, var(--night-glow) 100%); }

  .hero-title { position: absolute; left: 60px; top: 147px; width: 620px; text-align: center;
    color: var(--white); font-size: 48px; font-weight: 600; line-height: 66px; text-shadow: 0 2px 6px rgba(0,0,0,0.3); }
  .hero-cta { position: absolute; left: 298px; top: 387px; width: 144px; height: 49px; border: 2px solid var(--white);
    color: var(--white); font-size: 14px; font-weight: 600; display: flex; align-items: center; justify-content: center; text-decoration: none; }

  .auth-panel { position: absolute; left: 737px; top: 137px; width: 364px; height: 404px;
    border: 1px solid var(--white); background: rgba(110,140,220,0.45); padding: 7px; }
  .auth-card { position: absolute; left: 8px; top: 8px; width: 348px; height: 388px; background: var(--white); }
  .auth-tabs { position: absolute; left: 48px; top: 44px; width: 252px; height: 37px; border-bottom: 2px solid var(--brand-blue); display: flex; }
  .auth-tab { font-size: 15px; font-weight: 600; display: flex; align-items: center; justify-content: center; }
  .auth-tab--active { width: 110px; background: var(--brand-blue); color: var(--white); border-radius: 3px 3px 0 0; }
  .auth-tab--idle { flex: 1; color: var(--brand-blue); }

  .social-login { position: absolute; left: 48px; top: 86px; width: 252px; height: 37px; background: var(--social-blue);
    display: flex; align-items: center; color: var(--white); font-size: 12.5px; }
  .social-login-mark { width: 45px; height: 37px; background: var(--social-blue-dark); display: flex; align-items: center; justify-content: center; }
  .social-login-mark span { width: 10px; height: 10px; background: var(--white); }
  .social-login-label { padding-left: 19px; }

  .auth-or { position: absolute; left: 48px; top: 136px; width: 252px; text-align: center; font-size: 13px; color: var(--brand-blue); }
  .auth-field { position: absolute; left: 48px; width: 252px; height: 37px; border: 1px solid var(--brand-blue);
    font-family: inherit; font-size: 11px; color: var(--brand-blue); padding-left: 14px; display: flex; align-items: center; }
  .auth-field--email { top: 164px; }
  .auth-field--password { top: 212px; }
  .auth-forgot { position: absolute; left: 48px; top: 270px; width: 252px; text-align: center; font-size: 11px; font-weight: 600; color: var(--navy); }
  .auth-submit { position: absolute; left: 48px; top: 306px; width: 252px; height: 37px; background: var(--brand-blue);
    color: var(--white); font-size: 12.5px; font-weight: 600; display: flex; align-items: center; justify-content: center; gap: 6px; }

  .site-footer { position: absolute; left: 0; top: 629px; width: 1200px; text-align: center; color: var(--white); font-size: 12px; }
</style>
</head>
<body>
  <header class="site-header">
    <div class="brand"><span class="brand-square"></span><span class="brand-name">TallyNest</span></div>
    <nav class="main-nav">
      <a href="#" class="is-active" style="left:435px">Home</a>
      <a href="#" style="left:525px">About Us</a>
      <a href="#" style="left:634px">Features</a>
      <a href="#" style="left:740px">Pricing</a>
      <a href="#" style="left:833px">Contact</a>
    </nav>
    <a href="#" class="header-btn header-btn--login">LOG IN</a>
    <a href="#" class="header-btn header-btn--signup">SIGN UP</a>
  </header>

  <section class="hero" role="img" aria-label="Night club stage with disco balls, spotlights and a lit dance floor">
    <h1 class="hero-title">Bringing your club to the<br>Social Web.</h1>
    <a href="#" class="hero-cta">FIND OUT MORE</a>

    <div class="auth-panel">
      <div class="auth-card">
        <div class="auth-tabs">
          <div class="auth-tab auth-tab--active">LOG IN</div>
          <div class="auth-tab auth-tab--idle">SIGN UP</div>
        </div>
        <div class="social-login">
          <div class="social-login-mark"><span></span></div>
          <div class="social-login-label">Log in with Circlebook</div>
        </div>
        <div class="auth-or">or</div>
        <div class="auth-field auth-field--email">Your@example.com</div>
        <div class="auth-field auth-field--password">Your password</div>
        <div class="auth-forgot">Don't remember your Password ?</div>
        <div class="auth-submit">LOG IN
          <svg width="8" height="10" viewBox="0 0 8 10"><path d="M2 1l4 4-4 4" fill="none" stroke="#fff" stroke-width="1.6"/></svg>
        </div>
      </div>
    </div>
  </section>

  <footer class="site-footer">Copyright © TallyNest.2017. All rights reserved.</footer>
</body>
</html>
```